Frozen Yogurt Cup Design

We are looking for an art design for our 16 oz frozen yogurt cup for our company named, "Brindle: Frozen Yogurt Parlour." The target audience for a self-served yogurt place varies from children to adults, the final design should be versatile. We are looking for a design that incorporates our logo and the colors of lime green, yellow, orange, and royal blue. The final design should be modern, clean, and playful.

Target Market(s)

Ages 0 to 100

Industry/Entity Type

Royal

Requirements
Must have
• Attached logo design (out of the two designs please use the top one)

```html
<!DOCTYPE html>
<html lang="en">
<head>
<meta charset="utf-8">
<title>Brindle: Frozen Yogurt Parlour — Cup Wrap</title>
<link href="https://fonts.googleapis.com/css2?family=Fredoka:wght@600&display=swap" rel="stylesheet">
<style>
  :root {
    --canvas: #ffffff;
    --lime: #9ccc3c;
    --green: #6fb63f;
    --yellow: #fcd93a;
    --orange: #f7a830;
    --royal: #1f4f9a;
    --periwinkle: #a9b6dc;
    --label: #ffffff;
  }
  html, body {
    margin: 0;
    padding: 0;
    overflow: hidden;
    background: var(--canvas);
  }
  .canvas {
    width: 720px;
    height: 1200px;
    position: relative;
    background: var(--canvas);
    overflow: hidden;
  }
  .cup-wrap {
    position: absolute;
    left: 40px;
    top: 320px;
    width: 640px;
    height: 560px;
    overflow: hidden;
  }
  .wave-pattern {
    position: absolute;
    inset: 0;
    background:
      radial-gradient(ellipse at 0% 10%, var(--periwinkle) 0%, transparent 30%),
      radial-gradient(ellipse at 100% 100%, var(--royal) 0%, transparent 45%),
      linear-gradient(160deg, var(--orange) 0%, var(--yellow) 28%, var(--lime) 52%, var(--yellow) 70%, var(--green) 100%);
  }
  .label-oval {
    position: absolute;
    left: 166px;
    top: 166px;
    width: 260px;
    height: 196px;
    border-radius: 50%;
    background: var(--label);
    box-shadow: 14px 18px 22px rgba(40, 60, 20, 0.35);
    display: flex;
    flex-direction: column;
    align-items: center;
    justify-content: center;
    font-family: "Fredoka", sans-serif;
    font-weight: 600;
    color: var(--green);
    text-align: center;
  }
  .brand-name {
    font-size: 58px;
    line-height: 1;
    margin: 0;
  }
  .brand-tagline {
    font-size: 17px;
    line-height: 1.2;
    margin: 6px 0 0;
    letter-spacing: 0.02em;
  }
</style>
</head>
<body>
  <main class="canvas">
    <section class="cup-wrap">
      <div class="wave-pattern" role="img" aria-label="Playful diagonal wavy stripes in yellow, orange, lime green and royal blue with scattered white bubbles"></div>
      <div class="label-oval">
        <p class="brand-name">Brindle</p>
        <p class="brand-tagline">Frozen Yogurt Parlour</p>
      </div>
    </section>
  </main>
</body>
</html>
```